A poster for Vale Chiropractic's up coming powerful health workshop/seminar

I need a poster developed for Dr. Prent's upcoming Total Shape Reset and Armor Plating your Wellness seminar/workshop. This workshop will teach attendants how to shed pounds and rapidly reduce their waist size. Learn why weight loss doesn't work 99.9% of the time so that you can be the successful .1%. It's time to expose the LIES and reveal the TRUTH about the REAL causes of HEART DISEASE, DIABETES, CANCER, CHRONIC FATIGUE, ARTHRITIS, FIBROMYALGIA, and how to REVERSE/PREVENT this from ever happening to you or your family. The Insider Secrets to building your body into a health fortress unbreachable by sickness and disease. Learn to live and fufill your GOD-GIVEN health potential. Eliminate high bloodpressure, high cholesterol, diabetes, fatigue, chronic pain
Ending the WAR on sickness and disease by launching an unstoppable health offensive that will pummel any enemy of life and health.

I'm not a designer by any means, but was thinking of possible WAR theme, cammo, etc....just a thought. Not a requirement by any means
Updates

Dr. Prent has taken a look at all the submissions and has requested a few changes.

1. He wants the new map that has been added to the brief with Marlow Ridge College as a title above the map

2. He wants a section that describes what the attendees will gain at the seminar in bullet format.  Example:  Title....It's not about what you lose

                                                   I'ts about what you gain....

>The No-Hype, No- Gimmick  secrets for fast effective Weight loss

>How the top 3 disease killers, heart disease, cancer, and diabetes are linked to diet

>Tools and strategies to make 2012 the best year ever

The Seminar will be held at Marlow Ridge College, Tuesday January 3rd @ 6:30pm Open to Public

Target Market(s)

Adults 30-65

Industry/Entity Type

Building

Requirements
Should not have
• ruyrtur

```html
<!DOCTYPE html>
<html lang="en">
<head>
<meta charset="utf-8">
<title>Dr. Prent's Total Shape Reset</title>
<link rel="stylesheet" href="https://fonts.googleapis.com/css2?family=Montserrat:wght@200;300;500&family=Source+Sans+3:wght@400;600;700&display=swap">
<style>
  :root {
    --bg-dark: #1b1b1b;
    --bg-mid: #2f2f2f;
    --copper: #b5795a;
    --white: #ffffff;
    --muted: #d8d8d8;
    --figure-light: #efd9c4;
    --figure-shade: #cfb39a;
    --band: rgba(18, 18, 18, 0.9);
    --map-land: #5d6a62;
    --map-water: #7d8f96;
  }
  * { margin: 0; padding: 0; box-sizing: border-box; }
  html, body { width: 860px; height: 1200px; overflow: hidden; background: var(--bg-dark); }
  .poster {
    position: relative;
    width: 860px;
    height: 1200px;
    overflow: hidden;
    background: linear-gradient(90deg, var(--bg-dark) 0%, var(--bg-mid) 50%, var(--bg-dark) 100%);
  }
  .figure-area {
    position: absolute;
    left: 45px;
    top: 10px;
    width: 390px;
    height: 1190px;
    border-radius: 160px 160px 40px 40px;
    background: radial-gradient(ellipse at 45% 40%, var(--figure-light) 0%, var(--figure-shade) 55%, rgba(207,179,154,0) 82%);
    opacity: 0.85;
  }
  .presenter {
    position: absolute;
    right: 48px;
    top: 78px;
    font-family: "Montserrat", sans-serif;
    font-weight: 300;
    font-size: 58px;
    letter-spacing: 3px;
    color: var(--copper);
    line-height: 1;
  }
  .title {
    position: absolute;
    right: 40px;
    top: 196px;
    text-align: right;
    font-family: "Montserrat", sans-serif;
    font-weight: 200;
    color: var(--white);
    line-height: 0.78;
    text-transform: uppercase;
  }
  .title span { display: block; }
  .title .line-sm { font-size: 92px; letter-spacing: -1px; }
  .title .line-lg { font-size: 130px; letter-spacing: -2px; margin-top: 4px; }
  .details {
    position: absolute;
    left: 474px;
    top: 480px;
    width: 352px;
    font-family: "Source Sans 3", sans-serif;
    font-size: 17px;
    line-height: 22.5px;
    color: var(--white);
  }
  .details p { margin-bottom: 22.5px; }
  .details p:last-child { margin-bottom: 0; }
  .details strong { font-weight: 700; }

  .event-band {
    position: absolute;
    left: 0;
    bottom: 0;
    width: 860px;
    height: 92px;
    background: var(--band);
    border-top: 2px solid var(--copper);
    display: flex;
    align-items: center;
    gap: 18px;
    padding: 0 26px;
    font-family: "Source Sans 3", sans-serif;
    color: var(--white);
  }
  .gains { width: 448px; }
  .gains-title {
    font-family: "Montserrat", sans-serif;
    font-weight: 500;
    font-size: 12px;
    letter-spacing: 0.5px;
    color: var(--copper);
    text-transform: uppercase;
    margin-bottom: 4px;
  }
  .gains ul { list-style: none; }
  .gains li {
    font-size: 11.5px;
    line-height: 15px;
    color: var(--muted);
    padding-left: 12px;
    position: relative;
  }
  .gains li::before {
    content: "";
    position: absolute;
    left: 0;
    top: 5px;
    border-left: 6px solid var(--copper);
    border-top: 3.5px solid transparent;
    border-bottom: 3.5px solid transparent;
  }
  .venue { width: 150px; }
  .venue-title {
    font-weight: 600;
    font-size: 11.5px;
    line-height: 14px;
    margin-bottom: 3px;
    white-space: nowrap;
  }
  .venue-map {
    width: 150px;
    height: 54px;
    border: 1px solid var(--copper);
    background: linear-gradient(135deg, var(--map-land) 0%, var(--map-land) 62%, var(--map-water) 100%);
  }
  .when {
    flex: 1;
    text-align: right;
    line-height: 1.25;
  }
  .when-date {
    font-family: "Montserrat", sans-serif;
    font-weight: 300;
    font-size: 15px;
    color: var(--white);
  }
  .when-time {
    font-family: "Montserrat", sans-serif;
    font-weight: 500;
    font-size: 17px;
    color: var(--copper);
  }
  .when-note { font-size: 11.5px; color: var(--muted); text-transform: uppercase; letter-spacing: 1px; }
</style>
</head>
<body>
  <main class="poster">
    <div class="figure-area" role="img" aria-label="Full-length photo of a standing bald mannequin"></div>

    <div class="presenter">DR. PRENT'S</div>

    <h1 class="title">
      <span class="line-sm">Total</span>
      <span class="line-sm">Shape</span>
      <span class="line-lg">Reset</span>
    </h1>

    <section class="details">
      <p>This workshop will teach attendants how to shed pounds and rapidly reduce their waist size.</p>
      <p>Learn why weight loss doesn't work <strong>99.9%</strong> of the time so that you can be the successful <strong>1%.</strong></p>
      <p>It's time to expose the <strong>LIES</strong> and reveal the <strong>TRUTH</strong> about the <strong>REAL</strong> causes of <strong>HEART DISEASE, DIABETES, CANCER, CHRONIC FATIGUE, ARTHRITIS, FIBROMYALGIA</strong>, and how to <strong>REVERSE/PREVENT</strong> this from ever happening to you or your family.</p>
      <p>The Insider Secrets to building your body into a health fortress unbreachable by sickness and disease. Learn to live and fufill your <strong>GOD-GIVEN</strong> health potential.</p>
      <p>Eliminate high bloodpressure, high cholesterol, diabetes, fatigue, chronic pain.</p>
      <p>End the WAR on sickness and disease by launching an unstoppable health offensive that will pummel any enemy of life and health.</p>
    </section>

    <footer class="event-band">
      <div class="gains">
        <h2 class="gains-title">It's not about what you lose &mdash; it's about what you gain</h2>
        <ul>
          <li>The No-Hype, No-Gimmick secrets for fast effective weight loss</li>
          <li>How the top 3 disease killers, heart disease, cancer, and diabetes are linked to diet</li>
          <li>Tools and strategies to make 2012 the best year ever</li>
        </ul>
      </div>
      <div class="venue">
        <h3 class="venue-title">Marlow Ridge College</h3>
        <div class="venue-map" role="img" aria-label="Map showing the location of Marlow Ridge College"></div>
      </div>
      <div class="when">
        <div class="when-date">Tuesday, January 3rd</div>
        <div class="when-time">@ 6:30pm</div>
        <div class="when-note">Open to Public</div>
      </div>
    </footer>
  </main>
</body>
</html>
```